Catering Menu Package

I currently have a complete menu package, which we have redesigned as far as content, now I need to it put together in a catalog type format. It is essentially 10-12 pages in length, and will be sent for print production. Upon receiving a final edit
Updates

I have added an example gif to the project.

I did this free hand this basically what I am looking for. please change text and type to whatever you think would look best. This is a total rough design so, feel free to change any and everything. The text for the page is on the word documents. If you need more images let me know I am in the process of getting as many images uploaded for your use.

Reason: I figured we got a late jump with questions, so i am extending a few days .

Target Market(s)

The target market is business who wish to have catered luncheons, breakfasts , meetings

Industry/Entity Type

Catering

Requirements
Must have
• I have attached a copy of the text that what we want in the package, our logo, and i have also attached a catering package of another company to give you an idea what the finished product will be
Should not have
• It should not look identical to the example catering packages, these are for some inspiration we want our own design with the same type of look and feel

```html
<!DOCTYPE html>
<html lang="en">
<head>
<meta charset="utf-8">
<title>Desserts – Chesapeake Meadow Caterers</title>
<link rel="stylesheet" href="https://fonts.googleapis.com/css2?family=Fondamento&family=Pinyon+Script&display=swap">
<style>
  :root {
    --paper: #ece6da;
    --ink: #3b342d;
    --photo-dark: #5a1a17;
    --photo-red: #9c2a26;
    --photo-cream: #efe8de;
    --photo-white: #f7f4ef;
    --brand-square: #e2741f;
  }
  * { margin: 0; padding: 0; box-sizing: border-box; }
  html, body { width: 1200px; height: 928px; overflow: hidden; background: var(--paper); }
  .page {
    position: relative;
    width: 1200px;
    height: 928px;
    background: var(--paper);
    color: var(--ink);
    font-family: "Fondamento", serif;
    font-size: 17px;
    line-height: 24px;
  }
  .menu-title {
    position: absolute;
    left: 72px;
    top: 78px;
    font-family: "Pinyon Script", cursive;
    font-weight: 400;
    font-size: 46px;
    line-height: 56px;
  }
  .menu-section {
    position: absolute;
    left: 75px;
    width: 640px;
  }
  .menu-line {
    display: flex;
    justify-content: space-between;
    white-space: nowrap;
  }
  .price { width: 132px; text-align: left; }
  .s-cookies   { top: 141px; }
  .s-minis     { top: 185px; }
  .s-cheese    { top: 304px; }
  .s-sundae    { top: 398px; }
  .s-fountain  { top: 516px; }
  .brand {
    position: absolute;
    left: 72px;
    top: 720px;
    display: flex;
    align-items: flex-start;
    gap: 10px;
  }
  .brand-mark {
    width: 22px;
    height: 22px;
    background: var(--brand-square);
    margin-top: 4px;
  }
  .brand-name {
    font-family: "Fondamento", serif;
    font-size: 19px;
    line-height: 26px;
    color: var(--ink);
  }
  .dessert-photo {
    position: absolute;
    left: 774px;
    top: 0;
    width: 426px;
    height: 928px;
    background:
      radial-gradient(ellipse at 30% 45%, var(--photo-red) 0%, transparent 35%),
      radial-gradient(ellipse at 70% 70%, var(--photo-cream) 0%, transparent 45%),
      linear-gradient(160deg, var(--photo-red) 0%, var(--photo-white) 12%, var(--photo-dark) 40%, var(--photo-cream) 65%, var(--photo-dark) 100%);
  }
</style>
</head>
<body>
<main class="page">
  <h1 class="menu-title">Desserts</h1>

  <section class="menu-section s-cookies">
    <p class="menu-line"><span>Homemade Cookies, Brownies &amp; Blondies</span><span class="price">$X.XX per person</span></p>
  </section>

  <section class="menu-section s-minis">
    <p>Dessert Miniatures</p>
    <p>Homemade Cookies, Brownies, Blondies, Petit Fours,</p>
    <p class="menu-line"><span>Miniature Chocolate Mousse Cups &amp; Crème Puffs</span><span class="price">$X.XX per person</span></p>
    <p class="menu-line"><span>Strawberry Shortcake &amp; Chocolate Brownie Mousse Parfaits</span><span class="price">$X.XX per person</span></p>
  </section>

  <section class="menu-section s-cheese">
    <p>New York Style Cheesecake Bar</p>
    <p>With warm chocolate sauce, caramel, strawberries</p>
    <p class="menu-line"><span>Cherries &amp; whipped topping</span><span class="price">$X.XX per person</span></p>
  </section>

  <section class="menu-section s-sundae">
    <p>Ice Cream Sundae Bar</p>
    <p>Hand Dipped Ice Cream Cups. Served With Toppings:</p>
    <p>Chopped Nuts, Chocolate Chips, Crushed Cocoa Crème Cookies, Rainbow Sprinkles, Cherries,</p>
    <p>Whipped Topping, Chocolate Syrup, Caramel, Pineapple, Strawberry</p>
  </section>

  <section class="menu-section s-fountain">
    <p>Chocolate Fountain</p>
    <p>Milk Chocolate, Dark Chocolate Or White Chocolate.</p>
    <p>Marshmallows, Fresh Strawberries, Bananas, Pineapple, Cookies,</p>
    <p>Rice Crispy Treats, Pretzels, Angel Cake, Pound Cake</p>
  </section>

  <div class="brand">
    <span class="brand-mark"></span>
    <p class="brand-name">Chesapeake<br>Meadow<br>Caterers</p>
  </div>

  <div class="dessert-photo" role="img" aria-label="Photo of chocolate and white chocolate petit fours decorated as holiday gifts and candy canes on a white plate"></div>
</main>
</body>
</html>
```